Business card for apparel company. Specializing in fishing and boating performance wear. Main company name is Marlow Pelican Company, LLC brand name for apparel is TIDEWAKE. See website www.TidewakeBayline.com I will attach some logos to consider.

```html
<!DOCTYPE html>
<html lang="en">
<head>
<meta charset="utf-8">
<title>TIDEWAKE Business Card</title>
<link rel="stylesheet" href="https://fonts.googleapis.com/css2?family=Montserrat:wght@500;600;700;800&display=swap">
<style>
  :root {
    --page-bg: #1f272b;
    --front-navy: #2b4f68;
    --front-deep: #22435a;
    --card-white: #ffffff;
    --shirt-tint: #e4eef0;
    --ink: #2f4356;
    --stamp-blue: #a9d2ec;
    --mark-white: #ffffff;
  }
  * { box-sizing: border-box; margin: 0; padding: 0; }
  html, body {
    width: 1200px; height: 1200px; overflow: hidden;
    background: var(--page-bg);
    font-family: "Montserrat", sans-serif;
  }
  .sheet {
    position: relative; width: 1200px; height: 1200px;
    display: flex; flex-direction: column; align-items: center; justify-content: center; gap: 50px;
  }
  .card {
    position: relative; width: 720px; height: 410px;
    border-radius: 28px; overflow: hidden;
    box-shadow: 0 18px 40px rgba(0,0,0,.45);
  }
  /* Front */
  .card-front { background: var(--front-navy); }
  .front-photo {
    position: absolute; inset: 0;
    background: linear-gradient(135deg, #345b74 0%, var(--front-navy) 50%, var(--front-deep) 100%);
  }
  .front-mark {
    position: absolute; right: 40px; bottom: 60px;
    display: flex; align-items: center; gap: 22px;
    color: var(--mark-white); font-weight: 800; font-size: 84px; letter-spacing: 2px;
  }
  .front-mark .dot { width: 56px; height: 56px; border-radius: 50%; background: var(--mark-white); }
  /* Back */
  .card-back { background: var(--card-white); }
  .shirt-photo {
    position: absolute; left: 300px; top: 40px; width: 260px; height: 370px;
    background: linear-gradient(180deg, var(--shirt-tint), #d9e7ea);
    border-radius: 60px 60px 0 0; opacity: .8;
  }
  .stamp {
    position: absolute; left: 430px; top: 70px; width: 330px; height: 330px;
    border: 10px solid var(--stamp-blue); border-radius: 50%; opacity: .7;
    display: flex; justify-content: center; align-items: flex-start; padding-top: 52px;
  }
  .stamp-name { color: var(--stamp-blue); font-weight: 800; font-size: 34px; letter-spacing: 1px; }
  .brand {
    position: absolute; left: 48px; top: 58px;
    display: flex; align-items: center; gap: 16px;
    color: var(--ink); font-weight: 800; font-size: 54px; letter-spacing: 1px;
  }
  .brand .ring { width: 42px; height: 42px; border-radius: 50%; border: 6px solid var(--ink); }
  .company { position: absolute; left: 50px; top: 138px; color: var(--ink); font-weight: 600; font-size: 16px; }
  .contact { position: absolute; left: 48px; top: 236px; color: var(--ink); }
  .phone { font-weight: 700; font-size: 46px; line-height: 1.1; }
  .line { font-weight: 600; font-size: 17px; margin-top: 6px; }
  .social {
    position: absolute; right: 40px; bottom: 30px;
    display: flex; align-items: center; gap: 10px;
    color: var(--ink); font-weight: 500; font-size: 18px;
  }
  .social .icon { width: 28px; height: 28px; border-radius: 50%; background: var(--ink); }
</style>
</head>
<body>
<main class="sheet">
  <section class="card card-front">
    <div class="front-photo" role="img" aria-label="Underwater photo of a school of fish in deep blue water"></div>
    <div class="front-mark"><span class="dot"></span>TIDEWAKE</div>
  </section>

  <section class="card card-back">
    <div class="shirt-photo" role="img" aria-label="Light performance fishing shirt"></div>
    <div class="stamp"><span class="stamp-name">TIDEWAKE</span></div>
    <div class="brand"><span class="ring"></span>TIDEWAKE</div>
    <p class="company">Marlow Pelican Company, LLC</p>
    <div class="contact">
      <p class="phone">(480) 555-0143</p>
      <p class="line">hello@tidewakebayline.com &nbsp;-&nbsp; www.TidewakeBayline.com</p>
      <p class="line">2240 Harbor Reach Dr, Clearwater, FL 33755</p>
    </div>
    <div class="social">Find us on:
      <span class="icon"></span><span class="icon"></span><span class="icon"></span>
    </div>
  </section>
</main>
</body>
</html>
```